2.875 x 4 inch Ad for a Program Guide at Conference with 15,000

The ad needs to be 2.875 inches by 4 inches. I have attached some ideas. We definitely don't want a white background but we need the ad to visually jump off a page so our ad doesn't get lost. The mock-ups were something I put together so I could get a sense of what I wanted to say. I've also attached feedback from my business partners about these mock-ups.

Target Market(s)

Heads of Human Resources and Leadership Development, CEO's, COO's, and business owners.

Industry/Entity Type

Consulting

Font styles to use
Serif

Colors
6b449b
0355a3
0692cd
00a990
a64599
f37122

Requirements
Must have
• Colors from brand standards. Logo. Large lettering to be seen easily as a quarter page ad.
Nice to have
• Creativity... feeling of strength, warmth and business all at the same time.
Should not have
• Please note the updated logo. The name of the company is Vorrada Mindful Business.

```html
<!DOCTYPE html>
<html lang="en">
<head>
<meta charset="utf-8">
<title>Vorrada Mindful Business – Program Guide Ad</title>
<link href="https://fonts.googleapis.com/css2?family=Rozha+One&family=Tinos:wght@700&display=swap" rel="stylesheet">
<style>
  :root{
    --stage:#2a86c0;
    --brand-navy:#2b3a7a;
    --brand-blue:#0355a3;
    --brand-purple:#6b449b;
    --brand-magenta:#a64599;
    --brand-orange:#f37122;
    --white:#ffffff;
    --result-tint:#fde8f3;
  }
  *{margin:0;padding:0;box-sizing:border-box}
  html,body{width:1200px;height:1040px;overflow:hidden;background:var(--stage)}
  .ad{
    position:absolute;left:255px;top:40px;width:690px;height:960px;overflow:hidden;
    background:
      radial-gradient(circle at 8% 4%, #f7e27a 0%, rgba(247,226,122,0) 38%),
      radial-gradient(circle at 95% 10%, #f3d9f4 0%, rgba(243,217,244,0) 35%),
      radial-gradient(circle at 95% 85%, #c58ae6 0%, rgba(197,138,230,0) 45%),
      linear-gradient(170deg,#fbd9a8 0%,#f9c6c2 35%,#f59ac4 65%,#e48fd6 100%);
    box-shadow:0 10px 30px rgba(0,0,0,.25);
  }
  .brand{position:absolute;left:160px;top:32px;display:flex;align-items:center;gap:22px}
  .brand-dot{width:112px;height:112px;border-radius:50%;background:var(--brand-purple)}
  .brand-name{font-family:"Tinos",serif;font-weight:700;color:var(--brand-navy);line-height:1}
  .brand-name .word{display:block;font-size:52px;letter-spacing:1px}
  .brand-name .tag{display:block;font-size:17px;letter-spacing:2px;margin-top:6px}
  .splash{position:absolute;left:80px;top:170px;width:570px;height:540px}
  .headline{position:absolute;left:0;width:100%;text-align:center;font-family:"Rozha One",serif;color:var(--white);text-transform:uppercase;line-height:49px;font-size:50px}
  .headline.verbs{top:282px}
  .headline.focus{top:477px}
  .divider{position:absolute;left:268px;top:451px;width:154px;height:6px;border-radius:3px;background:var(--white)}
  .booth{position:absolute;left:268px;top:595px;width:136px;height:136px;border-radius:50%;background:var(--white);text-align:center;font-family:"Tinos",serif;font-weight:700;color:var(--brand-orange)}
  .booth .label{display:block;font-size:17px;margin-top:32px}
  .booth .number{display:block;font-family:"Rozha One",serif;font-weight:400;font-size:60px;line-height:52px}
  .learn{position:absolute;left:0;width:100%;top:738px;text-align:center;font-family:"Tinos",serif;font-weight:700;font-size:35px;color:var(--white);display:flex;justify-content:center;align-items:center;gap:6px}
  .learn .rule{width:52px;height:3px;background:var(--white)}
  .ribbon{position:absolute;left:47px;top:779px;width:596px;height:48px}
  .ribbon-text{position:absolute;left:0;width:100%;top:784px;text-align:center;font-family:"Tinos",serif;font-weight:700;font-size:32px;color:var(--white)}
  .result{position:absolute;left:0;width:100%;top:828px;text-align:center;font-family:"Tinos",serif;font-weight:700;font-size:54px;color:var(--result-tint)}
  .web{position:absolute;left:83px;top:904px;width:531px;height:80px;border-radius:40px;background:var(--white);text-align:center;font-family:"Tinos",serif;font-weight:700;font-size:42px;color:var(--brand-orange);padding-top:7px;letter-spacing:1px}
</style>
</head>
<body>
  <main class="ad">
    <div class="brand">
      <span class="brand-dot"></span>
      <span class="brand-name"><span class="word">VORRADA</span><span class="tag">MINDFUL BUSINESS</span></span>
    </div>

    <svg class="splash" viewBox="0 0 570 540" role="img" aria-label="Watercolour paint splash in magenta and violet behind the headline">
      <defs>
        <linearGradient id="splashFill" x1="0" y1="0" x2="1" y2="0">
          <stop offset="0" stop-color="#ff2d6f"/>
          <stop offset="0.45" stop-color="#d63fa8"/>
          <stop offset="0.75" stop-color="#7b47d6"/>
          <stop offset="1" stop-color="#a26be0"/>
        </linearGradient>
        <radialGradient id="splashFade" cx="0.5" cy="0.5" r="0.5">
          <stop offset="0.7" stop-color="#fff" stop-opacity="1"/>
          <stop offset="1" stop-color="#fff" stop-opacity="0"/>
        </radialGradient>
        <mask id="splashMask"><ellipse cx="285" cy="260" rx="280" ry="260" fill="url(#splashFade)"/></mask>
      </defs>
      <ellipse cx="285" cy="260" rx="275" ry="255" fill="url(#splashFill)" mask="url(#splashMask)"/>
    </svg>

    <h1 class="headline verbs">Explore<br>Develop<br>Strengthen</h1>
    <span class="divider"></span>
    <h2 class="headline focus">Leadership<br>&amp; Culture</h2>

    <div class="booth"><span class="label">BOOTH</span><span class="number">736</span></div>

    <p class="learn"><span class="rule"></span>Learn how:<span class="rule"></span></p>

    <svg class="ribbon" viewBox="0 0 596 48" aria-hidden="true">
      <polygon points="0,0 596,0 580,24 596,48 0,48 16,24" fill="var(--brand-blue)"/>
    </svg>
    <p class="ribbon-text">REAL Leadership + REAL Culture</p>

    <p class="result">= REAL RESULTS</p>

    <p class="web">www.vmbgroup.com</p>
  </main>
</body>
</html>
```